Reskinning of an eSport related app

We're looking for a redesign of an esport related community app. It should look very sharp and modern like trending fitness apps. Logo and general CI is done and fixed. UI needs to be reworked. In detail: - Overall GUI and Look and Feel - Playercard, Friends List, Achievement List - Icons for Achievements - Status system (Actually done via special borders) - Torvu Logo and dragon head are fixed, it can not be changed Actual Designs attached and so styles and look and feel we like. What we dont like very much at our actual design: - Look and feel of the borders. They need to look better and more modern. It is a break of the style - The look needs to be fresh, like fitness with asiatic touch - Good achievement icons are needed. Personal tryout link of the actual version: (It will mainly be used on mobile.) Https: //zq7arena.plomb. site / quick gear / people / 3a2d71c0-5b1e-4e2f-9c3a-7d8e0f1b2c44

```html
<!DOCTYPE html>
<html lang="en">
<head>
<meta charset="utf-8">
<title>Torvu – App Screens</title>
<link href="https://fonts.googleapis.com/css2?family=Open+Sans:wght@400;600;700&display=swap" rel="stylesheet">
<style>
  :root{
    --stage:#021d25;
    --screen-top:#2c5064;
    --screen-bottom:#36667e;
    --statusbar:#1e3b4b;
    --card:#46707f;
    --card-line:rgba(190,215,225,.45);
    --divider:rgba(190,215,225,.35);
    --text:#ffffff;
    --muted:#a9c1cc;
    --link:#2fb4ea;
    --slot:#333539;
    --silver:#e9eef1;
    --bronze:#e07a22;
    --gold:#f3c613;
  }
  *{box-sizing:border-box;margin:0;padding:0}
  html,body{width:1200px;height:1200px;overflow:hidden;background:var(--stage)}
  body{position:relative;font-family:"Open Sans",sans-serif;color:var(--text)}

  .screen{position:absolute;top:350px;width:246px;height:532px;overflow:hidden;
    background:linear-gradient(180deg,var(--screen-top),var(--screen-bottom))}
  .statusbar{position:absolute;left:0;top:0;width:100%;height:20px;background:var(--statusbar)}

  .brand{position:absolute;left:16px;top:36px;display:flex;align-items:center;gap:8px}
  .brand-dot{width:24px;height:24px;border-radius:50%;background:#0f2633}
  .brand-name{font-size:22px;font-weight:600;color:#0f2633;letter-spacing:.5px}

  /* list screen */
  .tabs{position:absolute;top:94px;left:0;width:100%;height:24px;border-bottom:1px solid var(--divider);font-size:11px}
  .tab{position:absolute;top:0;color:var(--muted)}
  .tab.is-active{color:var(--text);font-weight:600}
  .tab.is-active::after{content:"";position:absolute;left:10px;top:20px;width:18px;height:2px;background:var(--text)}
  .item{position:absolute;left:14px;width:217px;height:78px;background:var(--card);border:1px solid var(--card-line);border-radius:2px}
  .item-slot{position:absolute;left:12px;top:15px;width:48px;height:48px;border-radius:50%;background:var(--slot)}
  .item-slot.is-ringed{border:2px solid var(--silver)}
  .item-title{position:absolute;left:69px;top:11px;font-size:13px}
  .item-text{position:absolute;left:69px;top:32px;width:140px;font-size:8.6px;line-height:13px}

  /* profile screens */
  .backdrop{position:absolute;inset:20px 0 0 0;
    background:radial-gradient(ellipse at 70% 45%,rgba(20,40,52,.45),transparent 60%),
               radial-gradient(ellipse at 30% 70%,rgba(90,130,150,.35),transparent 55%)}
  .login{position:absolute;left:176px;top:43px;font-size:9.5px;color:var(--link)}
  .login-icon{position:absolute;left:206px;top:38px;width:24px;height:24px;border-radius:50%;background:#9aa8b8}
  .login-icon::before{content:"";position:absolute;left:8px;top:4px;width:8px;height:9px;border-radius:50%;background:#fff}
  .login-icon::after{content:"";position:absolute;left:5px;top:14px;width:14px;height:7px;border-radius:7px 7px 2px 2px;background:#fff}
  .avatar{position:absolute;left:64px;top:98px;width:117px;height:117px;border-radius:50%;padding:4px}
  .avatar-photo{width:100%;height:100%;border-radius:50%;background:radial-gradient(circle at 55% 40%,#8a8a8a,#3a3a3a 55%,#1c1c1c)}
  .tier-common .avatar{background:linear-gradient(140deg,#f5f7f8,#8d979d 50%,#eef2f4)}
  .tier-rare .avatar{background:linear-gradient(140deg,#f3a34a,#a24f10 50%,#f0a050)}
  .tier-epic .avatar{background:linear-gradient(140deg,#ffe36a,#c99600 50%,#fff08a)}
  .player-name{position:absolute;top:225px;width:100%;text-align:center;font-size:14px}
  .player-rank{position:absolute;top:243px;width:100%;text-align:center;font-size:10px}
  .section-rule{position:absolute;top:266px;left:0;width:100%;height:1px;background:var(--divider)}
  .section-title{position:absolute;left:14px;font-size:13px}
  .gear{position:absolute;left:14px;top:302px;width:202px;height:100px;border:1px solid var(--card-line);border-radius:2px;background:rgba(70,112,127,.35)}
  .gear-peek{position:absolute;left:233px;top:302px;width:20px;height:100px;border:1px solid var(--card-line);background:rgba(70,112,127,.35)}
  .gear-photo{position:absolute;left:11px;top:10px;width:70px;height:78px;background:linear-gradient(180deg,#f4f4f4,#e6e6e6);display:flex;align-items:center;justify-content:center}
  .gear-photo span{width:46px;height:62px;border-radius:12px 12px 4px 4px;background:#4d5a3c}
  .gear-name{position:absolute;left:89px;top:6px;font-size:13px}
  .gear-set{position:absolute;left:89px;top:27px;font-size:8.6px;color:var(--muted)}
  .gear-date{position:absolute;left:84px;top:78px;font-size:7.6px;font-weight:700}
  .medal{position:absolute;top:436px;width:40px;text-align:center}
  .medal svg{display:block;margin:0 auto}
  .medal-label{font-size:11px;margin-top:4px}
  .medal-common .medal-label{color:#fff}
  .medal-rare .medal-label{color:var(--bronze)}
  .medal-epic .medal-label{color:var(--gold)}
</style>
</head>
<body>

<!-- Item list -->
<section class="screen" style="left:59px">
  <div class="statusbar"></div>
  <div class="brand"><span class="brand-dot"></span><span class="brand-name">Torvu</span></div>
  <nav class="tabs">
    <span class="tab is-active" style="left:14px">Common</span>
    <span class="tab" style="left:86px">Rare</span>
    <span class="tab" style="left:131px">Epic</span>
    <span class="tab" style="left:174px">Upcoming</span>
  </nav>
  <article class="item" style="top:136px"><span class="item-slot is-ringed"></span><h3 class="item-title">Wolf</h3><p class="item-text">Lorem Ipsum is simply dummy text of the printing and type.</p></article>
  <article class="item" style="top:228px"><span class="item-slot is-ringed"></span><h3 class="item-title">Karte</h3><p class="item-text">Lorem Ipsum is simply dummy text of the printing and type.</p></article>
  <article class="item" style="top:320px"><span class="item-slot"></span><h3 class="item-title">Kampf</h3><p class="item-text">Lorem Ipsum is simply dummy text of the printing and type.</p></article>
  <article class="item" style="top:412px"><span class="item-slot"></span><h3 class="item-title">Rakete</h3><p class="item-text">Lorem Ipsum is simply dummy text of the printing and type.</p></article>
</section>

<!-- Player cards: common / rare / epic -->
<section class="screen tier-common" style="left:339px">
  <div class="backdrop" role="img" aria-label="Faint background photo of the player"></div>
  <div class="statusbar"></div>
  <div class="brand"><span class="brand-dot"></span><span class="brand-name">Torvu</span></div>
  <span class="login">Login</span><span class="login-icon"></span>
  <div class="avatar"><div class="avatar-photo" role="img" aria-label="Player profile photo"></div></div>
  <h2 class="player-name">Myface</h2><p class="player-rank">Warrier in traing</p>
  <div class="section-rule"></div>
  <h3 class="section-title" style="top:278px">Equipment</h3>
  <div class="gear"><div class="gear-photo" role="img" aria-label="Olive hooded jacket"><span></span></div><h4 class="gear-name">The wolf</h4><p class="gear-set">Set : Lorem Ipsum text</p><p class="gear-date">Equipped : 26 March 2019</p></div>
  <div class="gear-peek"></div>
  <h3 class="section-title" style="top:414px">Achievements</h3>
  <div class="medal medal-common" style="left:34px"><svg width="26" height="38" viewBox="0 0 26 38"><polygon points="6,20 2,36 7,32 11,36 13,22" fill="#e9eef1"/><polygon points="20,20 24,36 19,32 15,36 13,22" fill="#e9eef1"/><circle cx="13" cy="13" r="12" fill="#e9eef1"/><circle cx="13" cy="13" r="8.5" fill="#2c5064"/><text x="13" y="16.5" font-size="9" font-weight="700" text-anchor="middle" fill="#fff" font-family="Open Sans,sans-serif">10</text></svg><div class="medal-label">Common</div></div>
  <div class="medal medal-rare" style="left:102px"><svg width="26" height="38" viewBox="0 0 26 38"><polygon points="6,20 2,36 7,32 11,36 13,22" fill="#e07a22"/><polygon points="20,20 24,36 19,32 15,36 13,22" fill="#e07a22"/><circle cx="13" cy="13" r="12" fill="#e07a22"/><circle cx="13" cy="13" r="8.5" fill="#2c5064"/><text x="13" y="16.5" font-size="9" font-weight="700" text-anchor="middle" fill="#fff" font-family="Open Sans,sans-serif">5</text></svg><div class="medal-label">Rare</div></div>
  <div class="medal medal-epic" style="left:170px"><svg width="26" height="38" viewBox="0 0 26 38"><polygon points="6,20 2,36 7,32 11,36 13,22" fill="#f3c613"/><polygon points="20,20 24,36 19,32 15,36 13,22" fill="#f3c613"/><circle cx="13" cy="13" r="12" fill="#f3c613"/><circle cx="13" cy="13" r="8.5" fill="#2c5064"/><text x="13" y="16.5" font-size="9" font-weight="700" text-anchor="middle" fill="#fff" font-family="Open Sans,sans-serif">3</text></svg><div class="medal-label">Epic</div></div>
</section>

<section class="screen tier-rare" style="left:619px">
  <div class="backdrop" role="img" aria-label="Faint background photo of the player"></div>
  <div class="statusbar"></div>
  <div class="brand"><span class="brand-dot"></span><span class="brand-name">Torvu</span></div>
  <span class="login">Login</span><span class="login-icon"></span>
  <div class="avatar"><div class="avatar-photo" role="img" aria-label="Player profile photo"></div></div>
  <h2 class="player-name">Myface</h2><p class="player-rank">Warrier in traing</p>
  <div class="section-rule"></div>
  <h3 class="section-title" style="top:278px">Equipment</h3>
  <div class="gear"><div class="gear-photo" role="img" aria-label="Olive hooded jacket"><span></span></div><h4 class="gear-name">The wolf</h4><p class="gear-set">Set : Lorem Ipsum text</p><p class="gear-date">Equipped : 26 March 2019</p></div>
  <div class="gear-peek"></div>
  <h3 class="section-title" style="top:414px">Achievements</h3>
  <div class="medal medal-common" style="left:34px"><svg width="26" height="38" viewBox="0 0 26 38"><polygon points="6,20 2,36 7,32 11,36 13,22" fill="#e9eef1"/><polygon points="20,20 24,36 19,32 15,36 13,22" fill="#e9eef1"/><circle cx="13" cy="13" r="12" fill="#e9eef1"/><circle cx="13" cy="13" r="8.5" fill="#2c5064"/><text x="13" y="16.5" font-size="9" font-weight="700" text-anchor="middle" fill="#fff" font-family="Open Sans,sans-serif">10</text></svg><div class="medal-label">Common</div></div>
  <div class="medal medal-rare" style="left:102px"><svg width="26" height="38" viewBox="0 0 26 38"><polygon points="6,20 2,36 7,32 11,36 13,22" fill="#e07a22"/><polygon points="20,20 24,36 19,32 15,36 13,22" fill="#e07a22"/><circle cx="13" cy="13" r="12" fill="#e07a22"/><circle cx="13" cy="13" r="8.5" fill="#2c5064"/><text x="13" y="16.5" font-size="9" font-weight="700" text-anchor="middle" fill="#fff" font-family="Open Sans,sans-serif">5</text></svg><div class="medal-label">Rare</div></div>
  <div class="medal medal-epic" style="left:170px"><svg width="26" height="38" viewBox="0 0 26 38"><polygon points="6,20 2,36 7,32 11,36 13,22" fill="#f3c613"/><polygon points="20,20 24,36 19,32 15,36 13,22" fill="#f3c613"/><circle cx="13" cy="13" r="12" fill="#f3c613"/><circle cx="13" cy="13" r="8.5" fill="#2c5064"/><text x="13" y="16.5" font-size="9" font-weight="700" text-anchor="middle" fill="#fff" font-family="Open Sans,sans-serif">3</text></svg><div class="medal-label">Epic</div></div>
</section>

<section class="screen tier-epic" style="left:899px">
  <div class="backdrop" role="img" aria-label="Faint background photo of the player"></div>
  <div class="statusbar"></div>
  <div class="brand"><span class="brand-dot"></span><span class="brand-name">Torvu</span></div>
  <span class="login">Login</span><span class="login-icon"></span>
  <div class="avatar"><div class="avatar-photo" role="img" aria-label="Player profile photo"></div></div>
  <h2 class="player-name">Myface</h2><p class="player-rank">Warrier in traing</p>
  <div class="section-rule"></div>
  <h3 class="section-title" style="top:278px">Equipment</h3>
  <div class="gear"><div class="gear-photo" role="img" aria-label="Olive hooded jacket"><span></span></div><h4 class="gear-name">The wolf</h4><p class="gear-set">Set : Lorem Ipsum text</p><p class="gear-date">Equipped : 26 March 2019</p></div>
  <div class="gear-peek"></div>
  <h3 class="section-title" style="top:414px">Achievements</h3>
  <div class="medal medal-common" style="left:34px"><svg width="26" height="38" viewBox="0 0 26 38"><polygon points="6,20 2,36 7,32 11,36 13,22" fill="#e9eef1"/><polygon points="20,20 24,36 19,32 15,36 13,22" fill="#e9eef1"/><circle cx="13" cy="13" r="12" fill="#e9eef1"/><circle cx="13" cy="13" r="8.5" fill="#2c5064"/><text x="13" y="16.5" font-size="9" font-weight="700" text-anchor="middle" fill="#fff" font-family="Open Sans,sans-serif">10</text></svg><div class="medal-label">Common</div></div>
  <div class="medal medal-rare" style="left:102px"><svg width="26" height="38" viewBox="0 0 26 38"><polygon points="6,20 2,36 7,32 11,36 13,22" fill="#e07a22"/><polygon points="20,20 24,36 19,32 15,36 13,22" fill="#e07a22"/><circle cx="13" cy="13" r="12" fill="#e07a22"/><circle cx="13" cy="13" r="8.5" fill="#2c5064"/><text x="13" y="16.5" font-size="9" font-weight="700" text-anchor="middle" fill="#fff" font-family="Open Sans,sans-serif">5</text></svg><div class="medal-label">Rare</div></div>
  <div class="medal medal-epic" style="left:170px"><svg width="26" height="38" viewBox="0 0 26 38"><polygon points="6,20 2,36 7,32 11,36 13,22" fill="#f3c613"/><polygon points="20,20 24,36 19,32 15,36 13,22" fill="#f3c613"/><circle cx="13" cy="13" r="12" fill="#f3c613"/><circle cx="13" cy="13" r="8.5" fill="#2c5064"/><text x="13" y="16.5" font-size="9" font-weight="700" text-anchor="middle" fill="#fff" font-family="Open Sans,sans-serif">3</text></svg><div class="medal-label">Epic</div></div>
</section>

</body>
</html>
```